I need a book jacket cover for my historical fiction novel, Ravens of Tin. I have a picture for the front cover, the two gold crowns described in the book. I also have a picture for the back cover, a gilded skull cap wine vessel with its box and bottle of wine. The book is about Scythians from 2,000 years ago regrouping in the present to import heroin through Virginia Beach and the Outer Banks.

Font styles to use
Serif

Requirements
Must have
• Leave space on back cover for bar code.
• AUTHOR: Merrin Tal Voskuyl, MD
• Query short edition on back cover or jacket flap first 4 paragraphs describing the book.
• Same document paragraph describing Dr Voskuyl starting with, "For the past 40 years..."

```html
<!DOCTYPE html>
<html lang="en">
<head>
<meta charset="utf-8">
<title>Ravens of Tin — Book Jacket</title>
<link href="https://fonts.googleapis.com/css2?family=Cinzel:wght@400&family=Tinos:ital@0;1&display=swap" rel="stylesheet">
<style>
  :root {
    --page: #ffffff;
    --jacket-deep: #0f1d24;
    --jacket-mid: #1d3a3f;
    --jacket-glow: #4f9a8a;
    --title-ink: #f3f1ea;
    --title-shade: rgba(0,0,0,0.85);
    --author-ink: #f5efe0;
    --gold-light: #f1cf76;
    --gold-mid: #c8922f;
    --gold-dark: #6e4a12;
    --body-ink: #d9e2e2;
    --barcode-space: #b9bcbf;
    --photo-red: #a8323d;
    --photo-dark: #4a1219;
    --seam: rgba(0,0,0,0.35);
  }
  * { margin: 0; padding: 0; box-sizing: border-box; }
  html, body { width: 848px; height: 1200px; overflow: hidden; background: var(--page); }
  .canvas { position: relative; width: 848px; height: 1200px; }

  .jacket-bg {
    background:
      radial-gradient(ellipse 60% 45% at 50% 8%, var(--jacket-glow) 0%, rgba(79,154,138,0.35) 35%, rgba(0,0,0,0) 70%),
      radial-gradient(ellipse 80% 70% at 30% 70%, var(--jacket-mid) 0%, var(--jacket-deep) 80%);
  }

  /* Full spread */
  .spread { position: absolute; left: 29px; top: 30px; width: 796px; height: 337px; display: flex; overflow: hidden; }
  .back-panel { position: relative; width: 374px; height: 100%; }
  .spine { position: relative; width: 48px; height: 100%; border-left: 1px solid var(--seam); border-right: 1px solid var(--seam); }
  .front-panel { position: relative; width: 374px; height: 100%; }

  .back-photo {
    position: absolute; left: 184px; top: 23px; width: 109px; height: 97px;
    background: radial-gradient(ellipse at 60% 40%, var(--photo-red), var(--photo-dark));
  }
  .back-copy {
    position: absolute; left: 124px; top: 154px; width: 234px;
    font-family: "Tinos", serif; font-size: 5.5px; line-height: 7.6px;
    color: var(--body-ink); text-align: center;
  }
  .back-copy p { margin-bottom: 5px; }
  .back-copy .tagline { font-style: italic; }
  .barcode-space { position: absolute; left: 286px; top: 282px; width: 48px; height: 37px; background: var(--barcode-space); }

  .spine-title, .spine-author {
    position: absolute; left: 50%; white-space: nowrap; color: var(--title-ink);
    transform: translate(-50%, -50%) rotate(90deg);
  }
  .spine-title { top: 106px; font-family: "Cinzel", serif; font-size: 16px; letter-spacing: 1px; text-shadow: 1px 1px 2px var(--title-shade); }
  .spine-author { top: 275px; font-family: "Tinos", serif; font-size: 12px; color: var(--author-ink); }

  .author {
    position: absolute; left: 0; right: 0; text-align: center;
    font-family: "Tinos", serif; color: var(--author-ink);
    text-shadow: 1px 1px 2px rgba(0,0,0,0.6);
  }
  .ornament-band {
    position: absolute; left: 50%; transform: translateX(-50%);
    background: linear-gradient(90deg, rgba(200,146,47,0), var(--gold-mid) 12%, var(--gold-light) 50%, var(--gold-mid) 88%, rgba(200,146,47,0));
    border-radius: 4px;
  }
  .title {
    position: absolute; left: 0; right: 0; text-align: center;
    font-family: "Cinzel", serif; font-weight: 400; color: var(--title-ink);
    text-shadow: 2px 2px 3px var(--title-shade), -1px -1px 0 rgba(0,0,0,0.4);
  }
  .title span { display: block; }
  .crowns-photo {
    position: absolute;
    background: radial-gradient(ellipse at 45% 40%, var(--gold-light) 0%, var(--gold-mid) 45%, var(--gold-dark) 100%);
    border-radius: 50%;
    box-shadow: 0 10px 14px rgba(0,0,0,0.6);
  }

  .front-panel .author { top: 26px; font-size: 15px; line-height: 18px; }
  .front-panel .ornament-top { top: 56px; width: 152px; height: 8px; }
  .front-panel .title { top: 84px; font-size: 36px; line-height: 44px; }
  .front-panel .crowns-photo { left: 31px; top: 224px; width: 180px; height: 72px; }

  /* Standalone front cover */
  .front-cover { position: absolute; left: 35px; top: 765px; width: 310px; height: 412px; }
  .front-cover .author { top: 46px; font-size: 20px; line-height: 22px; }
  .front-cover .ornament-top { top: 76px; width: 232px; height: 9px; }
  .front-cover .title { top: 110px; font-size: 44px; line-height: 50px; }
  .front-cover .crowns-photo { left: 35px; top: 276px; width: 245px; height: 90px; }
</style>
</head>
<body>
<main class="canvas">

  <section class="spread jacket-bg" aria-label="Full jacket spread">
    <div class="back-panel">
      <div class="back-photo" role="img" aria-label="Photograph of a gilded skull cup wine vessel with its box and a bottle of wine"></div>
      <div class="back-copy">
        <p>Hundreds of years ago the Scythian horse lords buried their kings in gold. Now their heirs have returned, patient and ruthless, to reclaim a fortune hidden along the Atlantic shore.</p>
        <p class="tagline">When a gilded skull cup surfaces at auction, one doctor learns the past is never buried.</p>
        <p>Guided by clues in an ancient wine vessel, he follows a trail of tin ravens from the Black Sea steppe to the quiet marinas of Virginia Beach, where old loyalties and new money collide.</p>
        <p>Ravens of Tin brings the Scythians out of history and onto the Outer Banks, where a shipment of heroin is only the first of their ambitions.</p>
        <p>For the past 40 years Dr. Voskuyl has practiced medicine in Virginia Beach. He has published short stories and essays, lectured on ancient art, and travelled widely through the lands of the steppe. He lives on the coast with his family.</p>
      </div>
      <div class="barcode-space" aria-label="Space reserved for barcode"></div>
    </div>

    <div class="spine">
      <div class="spine-title">Ravens of Tin</div>
      <div class="spine-author">Merrin Tal Voskuyl, MD</div>
    </div>

    <div class="front-panel">
      <p class="author">Merrin Tal Voskuyl, MD</p>
      <div class="ornament-band ornament-top" role="img" aria-label="Gold scroll ornament"></div>
      <h1 class="title"><span>Ravens</span><span>of</span><span>Tin</span></h1>
      <div class="crowns-photo" role="img" aria-label="Photograph of two ancient gold leaf crowns"></div>
    </div>
  </section>

  <section class="front-cover jacket-bg" aria-label="Front cover">
    <p class="author">Merrin Tal Voskuyl, MD</p>
    <div class="ornament-band ornament-top" role="img" aria-label="Gold scroll ornament"></div>
    <h2 class="title"><span>Ravens</span><span>of</span><span>Tin</span></h2>
    <div class="crowns-photo" role="img" aria-label="Photograph of two ancient gold leaf crowns"></div>
  </section>

</main>
</body>
</html>
```